Craft Beer Can Label Design needed to update existing bottle label

We need an existing bottle label design changed and updated to a can label.I have attached 2 can ideas that i really love and also attached our existing bottle label, if you could have the same wording, barcodes and description of the bottle label (kelmoor lager) and change to look similar to the can designs.

The can dimensions will be different to the existing bottle label.
New can label dimensions-
Height= 88mm
Wide= 205mm

Target Market(s)

beer lovers

Colors

Designer to choose colors to be used in the design.

Requirements
Must have
• all the information on the existing Kelmoor Lager label which is in the design brief
• Also want to add the silver can colour like in the middle of the tansford brewing can so that it blends in with the can, as this is a label over the silver can and not a printed can.
Nice to have
• the same design concepts as the attached other 2 can designs
Should not have
• do not just copy the other cans, need to make it look original

```html
<!DOCTYPE html>
<html lang="en">
<head>
<meta charset="utf-8">
<title>Kelbrae Hoppy Lager – Can Label</title>
<link rel="stylesheet" href="https://fonts.googleapis.com/css2?family=Audiowide&family=Rubik+Wet+Paint&family=Roboto:wght@300;400;700&display=swap">
<style>
  :root {
    --page-bg: #ececec;
    --silver-light: #f4f4f5;
    --silver-dark: #c4c6ca;
    --skyline-light: #e2e2e3;
    --skyline-mid: #b4b4b6;
    --skyline-dark: #7e7e80;
    --label-black: #0b0b0b;
    --accent-orange: #e07a22;
    --text-white: #ffffff;
    --text-grey: #e9e9e9;
  }
  html, body {
    margin: 0;
    padding: 0;
    width: 1200px;
    height: 1039px;
    overflow: hidden;
    background: var(--page-bg);
  }
  .canvas {
    position: relative;
    width: 1200px;
    height: 1039px;
  }
  .can-label {
    position: absolute;
    left: 370px;
    top: 195px;
    width: 460px;
    height: 660px;
  }
  .label-art {
    position: absolute;
    inset: 0;
    width: 460px;
    height: 660px;
    display: block;
  }
  .brand-mark {
    position: absolute;
    left: 194px;
    top: 304px;
    width: 72px;
    height: 72px;
    display: flex;
    align-items: center;
    justify-content: center;
    font-family: "Roboto", sans-serif;
    font-weight: 700;
    font-size: 12px;
    color: var(--label-black);
  }
  .label-copy {
    position: absolute;
    left: 0;
    right: 0;
    top: 398px;
    text-align: center;
    color: var(--text-white);
  }
  .beer-name {
    margin: 0;
    font-family: "Audiowide", sans-serif;
    font-weight: 400;
    font-size: 60px;
    line-height: 66px;
    letter-spacing: 6px;
    color: var(--text-grey);
  }
  .beer-style {
    margin: 8px 0 0;
    font-family: "Rubik Wet Paint", sans-serif;
    font-size: 34px;
    line-height: 40px;
    font-weight: 400;
  }
  .beer-details {
    margin: 16px 0 0;
    padding: 0;
    list-style: none;
    font-family: "Roboto", sans-serif;
    font-weight: 300;
    font-size: 14px;
    line-height: 23px;
  }
</style>
</head>
<body>
<main class="canvas">
  <section class="can-label">
    <svg class="label-art" viewBox="0 0 460 660" xmlns="http://www.w3.org/2000/svg">
      <defs>
        <linearGradient id="silverBody" x1="0" y1="0" x2="1" y2="0">
          <stop offset="0" stop-color="var(--silver-dark)"/>
          <stop offset="0.3" stop-color="var(--silver-light)"/>
          <stop offset="0.7" stop-color="var(--silver-light)"/>
          <stop offset="1" stop-color="var(--silver-dark)"/>
        </linearGradient>
        <linearGradient id="skylineTone" x1="0" y1="0" x2="0" y2="1">
          <stop offset="0" stop-color="var(--skyline-light)" stop-opacity="0"/>
          <stop offset="0.35" stop-color="var(--skyline-mid)" stop-opacity="0.55"/>
          <stop offset="1" stop-color="var(--skyline-dark)" stop-opacity="0.95"/>
        </linearGradient>
      </defs>
      <rect class="silver-body" x="0" y="0" width="460" height="660" fill="url(#silverBody)"/>
      <rect class="top-stripe" x="0" y="0" width="460" height="10" fill="var(--accent-orange)"/>
      <polygon class="skyline-area" role="img" aria-label="Grey city skyline of tower blocks with a tall observation tower rising at centre"
               points="0,125 460,125 460,262 230,335 0,262" fill="url(#skylineTone)"/>
      <polyline class="chevron-stripe" points="0,266 230,340 460,266" fill="none" stroke="var(--accent-orange)" stroke-width="9"/>
      <polygon class="black-band" points="0,275 230,349 460,275 460,628 0,628" fill="var(--label-black)"/>
      <rect class="bottom-stripe-thin" x="0" y="620" width="460" height="3" fill="var(--accent-orange)"/>
      <rect class="bottom-stripe" x="0" y="628" width="460" height="9" fill="var(--accent-orange)"/>
      <circle class="brand-badge" cx="230" cy="340" r="36" fill="var(--text-white)" stroke="var(--label-black)" stroke-width="4"/>
    </svg>
    <div class="brand-mark">Fernbank</div>
    <div class="label-copy">
      <h1 class="beer-name">KELBRAE</h1>
      <h2 class="beer-style">HOPPY LAGER</h2>
      <ul class="beer-details">
        <li>Handicrafted in Tasmania</li>
        <li>ABV 5.8%</li>
        <li>IBU 50</li>
        <li>330 ml</li>
      </ul>
    </div>
  </section>
</main>
</body>
</html>
```